Candy Bar Desgin

We need a postcard desgin for my new company. I just started a Candy bar/buffet called Candy bar By Pip Pip. My motto is Candy Bar by Pip Pip for the tip top. I will be attending a bridal show where I can display my work so there will be brides there. So I want something to pop. Maybe can add vases filled with candy. Add 20% off an event you book for attending the bridal show. I want colors. Candy colors. My company also do chocolate fountain bars as well. My website to add is www.candybarbypippip.example
Email candybarbypippip@mailbox.example
Phone 555-014-2286

Target Market(s)

Brides

Industry/Entity Type

It Company

Requirements
Must have
• Must have my motto. And my contact information
Should not have
• No old style don't like times new roman. Use fun fonts

```html
<!DOCTYPE html>
<html lang="en">
<head>
<meta charset="utf-8">
<title>Candy Bar by Pip Pip – Postcard Back</title>
<link rel="stylesheet" href="https://fonts.googleapis.com/css2?family=Playball&family=Didact+Gothic&display=swap">
<style>
  :root {
    --paper: #ffffff;
    --candy-pink: #ee2a6b;
    --teal: #00afc6;
    --ink: #1a1a1a;
    --white: #ffffff;
    --photo-pink: #e98ab4;
    --photo-lilac: #a99ad8;
    --photo-cream: #efe6da;
  }
  * { box-sizing: border-box; margin: 0; padding: 0; }
  html, body { width: 1200px; height: 930px; overflow: hidden; background: var(--paper); }
  .postcard {
    position: relative;
    width: 1200px;
    height: 930px;
    background: var(--paper);
    font-family: "Didact Gothic", "Century Gothic", sans-serif;
    color: var(--ink);
  }
  .candy-photo {
    position: absolute;
    left: 0; top: 0;
    width: 294px; height: 299px;
    background:
      radial-gradient(ellipse 30% 45% at 30% 50%, var(--photo-pink), transparent 70%),
      radial-gradient(ellipse 25% 25% at 70% 55%, var(--photo-lilac), transparent 70%),
      linear-gradient(160deg, var(--photo-cream) 0%, var(--photo-lilac) 55%, var(--photo-pink) 100%);
  }
  .tagline-panel {
    position: absolute;
    left: 309px; top: 0;
    width: 527px; height: 229px;
    background: var(--candy-pink);
    display: flex;
    align-items: flex-start;
    justify-content: center;
    padding-top: 64px;
  }
  .tagline {
    font-family: "Playball", cursive;
    color: var(--white);
    font-size: 26px;
    line-height: 41px;
    text-align: center;
  }
  .stamp-box {
    position: absolute;
    left: 913px; top: 59px;
    width: 236px; height: 224px;
    border: 3px dotted var(--ink);
    display: flex;
    align-items: center;
    justify-content: center;
    text-align: center;
    font-size: 34px;
    line-height: 43px;
  }
  .message-area {
    position: absolute;
    left: 30px; top: 350px;
    width: 460px;
    text-align: center;
  }
  .motto {
    font-family: "Playball", cursive;
    color: var(--candy-pink);
    font-size: 31px;
    line-height: 40px;
  }
  .offer {
    margin: 26px auto 0;
    width: 380px;
    padding: 16px 10px;
    background: var(--candy-pink);
    color: var(--white);
    font-size: 19px;
    line-height: 26px;
  }
  .offer-amount {
    display: block;
    font-size: 40px;
    line-height: 46px;
  }
  .services-note {
    margin-top: 18px;
    font-size: 18px;
    line-height: 24px;
    color: var(--teal);
  }
  .contact {
    margin-top: 22px;
    list-style: none;
    font-size: 18px;
    line-height: 30px;
  }
  .contact-label {
    color: var(--candy-pink);
  }
  .divider {
    position: absolute;
    left: 522px; top: 337px;
    width: 4px; height: 424px;
    background: repeating-linear-gradient(to bottom, var(--ink) 0 2px, transparent 2px 4px);
  }
  .address-label {
    position: absolute;
    left: 591px; top: 452px;
    font-size: 34px;
    line-height: 1;
  }
  .address-line {
    position: absolute;
    left: 649px;
    width: 499px;
    height: 2px;
    background: var(--ink);
  }
  .address-line--1 { top: 482px; }
  .address-line--2 { top: 553px; }
  .address-line--3 { top: 629px; }
  .address-line--4 { top: 702px; }
  .services-band {
    position: absolute;
    left: 0; top: 859px;
    width: 1200px; height: 71px;
    background: var(--teal);
    color: var(--white);
    font-size: 17.4px;
    line-height: 71px;
    padding-left: 53px;
    white-space: nowrap;
  }
</style>
</head>
<body>
  <main class="postcard">
    <div class="candy-photo" role="img" aria-label="Glass apothecary jars filled with pink, purple and white candy on a pink polka-dot table"></div>

    <section class="tagline-panel">
      <p class="tagline">Candy Bar by Pip Pip will add fun and cool<br>to your next event and bring you and your guest<br>back to your childhood roots</p>
    </section>

    <div class="stamp-box">Place<br>Stamp<br>Here</div>

    <section class="message-area">
      <p class="motto">Candy Bar by Pip Pip for the tip top</p>
      <p class="offer"><span class="offer-amount">20% OFF</span>any event you book at the bridal show</p>
      <p class="services-note">Candy bars, buffets &amp; chocolate fountain bars</p>
      <ul class="contact">
        <li><span class="contact-label">Web</span> www.candybarbypippip.example</li>
        <li><span class="contact-label">Email</span> candybarbypippip@mailbox.example</li>
        <li><span class="contact-label">Phone</span> 555-014-2286</li>
      </ul>
    </section>

    <div class="divider"></div>

    <p class="address-label">To.</p>
    <div class="address-line address-line--1"></div>
    <div class="address-line address-line--2"></div>
    <div class="address-line address-line--3"></div>
    <div class="address-line address-line--4"></div>

    <footer class="services-band">Birthday Parties - Weddings - Graduations - Sweet 16s - Baby showers - Bridal Showers - Holiday Parties - Corporate Events - Bar and Bat Mitzvahs</footer>
  </main>
</body>
</html>
```